Venture firm needs flyer to attract Sales Professionals as Advisors

Creation of either a pdf Flyer or Brochure.
The target audience are senior sales professionals of the Information Technology industry. The flyer needs to come across highly professional, business oriented, positive. Text for the brochure is attached. The colors/graphics should align with Brindmore Capital corporate appearance: www.brindmore.capital

Target Market(s)

Sales Professionals in the Information Technology Industry

Industry/Entity Type

Information Technology

Font styles to use
• Raleway

Requirements
Must have
• fitting the corporate look and feel: www.brindmore.capital

```html
<!DOCTYPE html>
<html lang="en">
<head>
<meta charset="utf-8">
<title>Brindmore Capital – BSC Flyer</title>
<link href="https://fonts.googleapis.com/css2?family=Raleway:wght@400;600&display=swap" rel="stylesheet">
<style>
  :root {
    --canvas: #ffffff;
    --navy: #0f3a5f;
    --band: #3a6f9a;
    --bar: #8aa9c3;
    --label: #d3dde7;
    --text-light: #eef3f8;
    --photo-cool: #9aa7b8;
    --photo-cool-light: #b4bfcc;
  }
  * { margin: 0; padding: 0; box-sizing: border-box; }
  html, body {
    width: 1200px; height: 1000px; overflow: hidden;
    background: var(--canvas);
    font-family: "Raleway", sans-serif;
  }
  .flyer {
    position: absolute; left: 302px; top: 79px;
    width: 595px; height: 841px;
    background: var(--navy);
  }
  .section-bar {
    position: absolute; left: 0; width: 595px; height: 37px;
    background: var(--bar);
  }
  .section-label {
    position: absolute; left: 0; top: 0; width: 176px; height: 37px;
    background: var(--label);
  }
  .section-title {
    position: absolute; top: 7px;
    font-size: 20px; font-weight: 600; color: var(--navy);
    white-space: nowrap;
  }
  .section-body {
    position: absolute; left: 0; width: 595px;
    background: var(--band);
  }
  .copy {
    position: absolute;
    font-size: 11.2px; line-height: 14.5px; color: var(--text-light);
  }
  .copy p + p { margin-top: 14.5px; }
  .photo {
    position: absolute; top: 551px; height: 167px;
    background: linear-gradient(180deg, var(--photo-cool-light) 0%, var(--photo-cool) 100%);
  }
  .photo-team { left: 28px; width: 221px; }
  .photo-summit { left: 269px; width: 298px; }
  .closing { top: 754px; left: 32px; width: 505px; }
  .footer-rule {
    position: absolute; left: 0; top: 812px; width: 595px; height: 8px;
    background: var(--label);
  }
</style>
</head>
<body>
  <main class="flyer">
    <section>
      <div class="section-bar" style="top:49px">
        <div class="section-label"></div>
        <h2 class="section-title" style="left:36px">How it works</h2>
      </div>
      <div class="section-body" style="top:86px;height:130px">
        <div class="copy" style="left:36px;top:7px;width:524px">
          <p>BSC members will be introduced to Brindmore Capital’ client and portfolio companies. This unique ability to learn about latest technology innovation keeps the participants up to date with industry trends and could open interesting earning or employment opportunities.</p>
          <p>Once exposed to a specific vendor, BSC members can decide if and how they would like to get further involved. Dependent on the interest level for the specific technology, the ability to offer a solution to a known customer problem or the sheer interest to develop new business, BSC members can participate in two ways:</p>
        </div>
      </div>
    </section>

    <section>
      <div class="section-bar" style="top:259px">
        <div class="section-label"></div>
        <h2 class="section-title" style="left:32px">As Associates</h2>
      </div>
      <div class="section-body" style="top:296px;height:57px">
        <div class="copy" style="left:32px;top:16px;width:500px">
          <p>Associates are actively selling and promoting one or more Brindmore Capital’ portfolio companies. This could be an employment or a freelance opportunity.</p>
        </div>
      </div>
    </section>

    <section>
      <div class="section-bar" style="top:396px">
        <div class="section-label"></div>
        <h2 class="section-title" style="left:27px">As Advisors</h2>
      </div>
      <div class="section-body" style="top:433px;height:79px">
        <div class="copy" style="left:27px;top:7px;width:538px">
          <p>Advisors offer their contacts and knowledge about customers to Associates.<br>Advisors could create leads, support with introductions, explain customer organization and processes etc. They will be compensated by Associates with a pre-negotiated % of commission of a future sale that was supported by the Advisor.</p>
        </div>
      </div>
    </section>

    <div class="photo photo-team" role="img" aria-label="Photo of a bobsleigh team racing down an icy track"></div>
    <div class="photo photo-summit" role="img" aria-label="Photo of climbers crossing a snowy mountain ridge"></div>

    <div class="copy closing">
      <p>Whatever level of involvement a BSC member seeks there is plenty of opportunity to be rewarded for working with fellow Sales Professionals and Great Startups on the forefront of technical innovation.</p>
    </div>

    <div class="footer-rule"></div>
  </main>
</body>
</html>
```